Velqor Group: Business Card for a high end technology company

We need a cool new design for our business cards using our cloud logo. We are a technology consulting business. We pride ourselves on be the best of the best. We mainly focus on cloud solutions and managed services. We need a business card that sets us apart from the other technology companies in the area and allows us to stand out.

Target Market(s)

Technology departments, CIO, CEOs, and Information Technology Staff.

Industry/Entity Type

Information Technology

Contact Information for Business Card

Must have the logo and our name.
Must have employee name, email address, office phone, cell phone and website.
Need to have all info on one side a cool design on backside.

Font styles to use
Serif
Sans Serif

Requirements
Must have
• Must have the logo and our name.
• Must have employee name, email address, office phone, cell phone and website.
• Need to have all info on one side a cool design on back side.
• Must be a crisp clean design, not too busy or confusing.

```html
<!DOCTYPE html>
<html lang="en">
<head>
<meta charset="utf-8">
<title>Velqor Group – Business Card</title>
<link href="https://fonts.googleapis.com/css2?family=Montserrat:wght@400;700&family=Open+Sans:wght@400;700&display=swap" rel="stylesheet">
<style>
  :root {
    --page: #2b2b2d;
    --card-black: #050505;
    --brand-blue: #3a8ee0;
    --brand-blue-deep: #1f6fc4;
    --brand-blue-light: #4c9de8;
    --band-grey: #3b4350;
    --white: #ffffff;
  }
  * { margin: 0; padding: 0; box-sizing: border-box; }
  html, body {
    width: 1200px; height: 900px; overflow: hidden;
    background: var(--page);
  }
  .canvas { position: relative; width: 1200px; height: 900px; }
  .card {
    position: absolute; left: 250px; width: 700px; height: 400px;
    border-radius: 22px; overflow: hidden; background: var(--card-black);
  }
  .card--front { top: 35px; }
  .card--back { top: 465px; }

  .wordmark {
    display: flex; align-items: center; gap: 16px;
    font-family: "Montserrat", sans-serif; font-weight: 400;
    font-size: 52px; color: var(--white); letter-spacing: 1px;
    white-space: nowrap;
  }
  .wordmark__dot {
    width: 40px; height: 40px; border-radius: 50%; background: var(--brand-blue);
    flex: none;
  }
  .card--front .brand {
    position: absolute; inset: 0;
    display: flex; flex-direction: column; align-items: center; justify-content: center; gap: 14px;
  }
  .web-address {
    font-family: "Open Sans", sans-serif; font-weight: 700;
    font-size: 18px; color: var(--white); letter-spacing: 0.5px;
  }

  .card--back .panel { position: absolute; inset: 0; }
  .card--back .brand {
    position: absolute; left: 20px; top: 0; height: 400px; width: 330px;
    display: flex; align-items: center; justify-content: center;
  }
  .card--back .wordmark { font-size: 40px; gap: 14px; letter-spacing: 0.5px; }
  .card--back .wordmark__dot { width: 34px; height: 34px; }

  .contact {
    position: absolute; right: 40px; top: 70px; text-align: right;
    font-family: "Open Sans", sans-serif; color: var(--white);
  }
  .contact__name { font-weight: 700; font-size: 24px; letter-spacing: 0.5px; text-transform: uppercase; }
  .contact__role { font-size: 15px; margin-bottom: 16px; }
  .contact__line {
    display: flex; justify-content: flex-end; align-items: center; gap: 9px;
    font-size: 15px; line-height: 26px; white-space: nowrap;
  }
  .contact__icon { width: 14px; height: 14px; fill: none; stroke: var(--white); stroke-width: 1.8; flex: none; }
</style>
</head>
<body>
<main class="canvas">

  <section class="card card--front">
    <div class="brand">
      <div class="wordmark"><span class="wordmark__dot"></span><span>Velqor Group</span></div>
      <div class="web-address">www.velqorgroup.com</div>
    </div>
  </section>

  <section class="card card--back">
    <svg class="panel" width="700" height="400" viewBox="0 0 700 400">
      <defs>
        <linearGradient id="blueFill" x1="0" y1="0" x2="1" y2="1">
          <stop offset="0" stop-color="var(--brand-blue-deep)"/>
          <stop offset="0.6" stop-color="var(--brand-blue)"/>
          <stop offset="1" stop-color="var(--brand-blue-light)"/>
        </linearGradient>
      </defs>
      <path d="M345 0 C 415 70, 435 220, 405 400 L 700 400 L 700 0 Z" fill="var(--band-grey)"/>
      <path d="M370 0 C 440 70, 460 220, 428 400 L 700 400 L 700 0 Z" fill="url(#blueFill)"/>
    </svg>

    <div class="brand">
      <div class="wordmark"><span class="wordmark__dot"></span><span>Velqor Group</span></div>
    </div>

    <div class="contact">
      <div class="contact__name">Daniel Rourke</div>
      <div class="contact__role">Director</div>
      <div class="contact__line">555.210.4836
        <svg class="contact__icon" viewBox="0 0 16 16"><path d="M3 2 L6 2 L7 5 L5.5 6.5 C6.5 8.5 7.5 9.5 9.5 10.5 L11 9 L14 10 L14 13 C8 13.5 2.5 8 3 2 Z"/></svg>
      </div>
      <div class="contact__line">555.210.7192
        <svg class="contact__icon" viewBox="0 0 16 16"><rect x="4.5" y="1.5" width="7" height="13" rx="1.5"/><line x1="7" y1="12" x2="9" y2="12"/></svg>
      </div>
      <div class="contact__line">info@velqorgroup.com
        <svg class="contact__icon" viewBox="0 0 16 16"><rect x="1.5" y="3.5" width="13" height="9" rx="1"/><path d="M1.5 4 L8 9 L14.5 4"/></svg>
      </div>
      <div class="contact__line">www.velqorgroup.com
        <svg class="contact__icon" viewBox="0 0 16 16"><circle cx="8" cy="8" r="6.5"/><ellipse cx="8" cy="8" rx="3" ry="6.5"/><line x1="1.5" y1="8" x2="14.5" y2="8"/></svg>
      </div>
    </div>
  </section>

</main>
</body>
</html>
```